need a clean, modern job advertisement designed for social media (Facebook & Instagram).

The post is to advertise two positions:
• Leading Hand Boilermaker
• Dragline Fitter
We want the design to match our KRT Plant Services branding: blue, white, strong, professional, mining-industry style.
What the design should include:
Bold headline: “WE’RE HIRING”
Sub-headline: “Leading Hand Boilermaker & Dragline Fitter”
Key points:
• Bowen Basin based
• Dragline & shovel maintenance
• Great pay + long-term work
• Locally owned & operated
KRT logo placed cleanly
Space for 1–2 images (boilermaking or dragline work)
Design style:
Strong and industrial
Blue/white colour scheme
Easy to read at a glance
Suitable for a square 1080×1080 design

```html
<!DOCTYPE html>
<html lang="en">
<head>
<meta charset="utf-8">
<title>KRT Plant Services – We are Hiring</title>
<link rel="stylesheet" href="https://fonts.googleapis.com/css2?family=Bebas+Neue&family=Poppins:wght@400;600;700&display=swap">
<style>
  :root {
    --page-grey: #999999;
    --paper: #ffffff;
    --sky: #00adef;
    --sky-deep: #0a7fb8;
    --ink: #050505;
    --glow: #bfe9fd;
  }
  * { margin: 0; padding: 0; box-sizing: border-box; }
  html, body { width: 1200px; height: 1149px; overflow: hidden; background: var(--page-grey); }
  .canvas { position: relative; width: 1200px; height: 1149px; }
  .artboard { position: absolute; left: 133px; top: 107px; width: 934px; height: 934px; background: var(--paper); overflow: hidden; }
  .shapes { position: absolute; left: 0; top: 0; }
  .brand {
    position: absolute; left: 214px; top: 262px; display: flex; align-items: center; gap: 12px;
    font-family: "Poppins", sans-serif; font-weight: 700; font-size: 27px; color: var(--sky); line-height: 1;
  }
  .brand-dot { width: 34px; height: 34px; border-radius: 50%; background: var(--sky); }
  .headline-top {
    position: absolute; left: 203px; top: 394px; font-family: "Poppins", sans-serif; font-weight: 700;
    font-size: 70px; letter-spacing: -1px; color: var(--ink); line-height: 1;
  }
  .headline-main {
    position: absolute; left: 201px; top: 457px; font-family: "Poppins", sans-serif; font-weight: 700;
    font-size: 128px; letter-spacing: -2.5px; color: var(--sky); line-height: 1;
  }
  .role-lead {
    position: absolute; left: 211px; top: 614px; font-family: "Bebas Neue", sans-serif; font-size: 46px;
    letter-spacing: 12px; color: var(--sky); line-height: 1;
  }
  .role-title {
    position: absolute; left: 211px; top: 663px; font-family: "Bebas Neue", sans-serif; font-size: 56px;
    color: var(--ink); line-height: 0.82; letter-spacing: -0.3px; font-weight: 400;
  }
  .perks {
    position: absolute; left: 211px; top: 780px; list-style: none; font-family: "Poppins", sans-serif;
    font-size: 21.5px; color: var(--ink); line-height: 29px;
  }
  .perks li::before { content: "•"; margin-right: 8px; }
  .apply-label {
    position: absolute; left: 337px; top: 940px; width: 269px; height: 49px; display: flex; align-items: center;
    justify-content: center; font-family: "Bebas Neue", sans-serif; font-size: 38px; color: var(--paper); padding-top: 4px;
  }
  .visit {
    position: absolute; left: 627px; top: 944px; font-family: "Poppins", sans-serif; font-size: 19px;
    letter-spacing: 14.6px; color: var(--ink); line-height: 1; white-space: nowrap;
  }
  .url {
    position: absolute; left: 626px; top: 969px; font-family: "Poppins", sans-serif; font-weight: 700;
    font-size: 24px; color: var(--ink); line-height: 1;
  }
</style>
</head>
<body>
<div class="canvas">
  <div class="artboard"></div>

  <svg class="shapes" width="1200" height="1149" viewBox="0 0 1200 1149">
    <defs>
      <linearGradient id="bandTop" x1="0" x2="1" y1="0" y2="0">
        <stop offset="0" stop-color="#00adef"/><stop offset="0.6" stop-color="#0a6a98"/><stop offset="1" stop-color="#000"/>
      </linearGradient>
      <linearGradient id="diagBlue" x1="0" y1="0" x2="1" y2="1">
        <stop offset="0" stop-color="#00adef"/><stop offset="0.55" stop-color="#0b77ad"/><stop offset="1" stop-color="#00adef"/>
      </linearGradient>
      <linearGradient id="bandBottom" x1="0" x2="1">
        <stop offset="0" stop-color="#000"/><stop offset="0.45" stop-color="#0a6a98"/><stop offset="1" stop-color="#00adef"/>
      </linearGradient>
      <radialGradient id="glow" cx="0.5" cy="0.5" r="0.5">
        <stop offset="0" stop-color="#7fd3fa"/><stop offset="0.6" stop-color="#bfe9fd"/><stop offset="1" stop-color="#ffffff" stop-opacity="0"/>
      </radialGradient>
      <linearGradient id="photoWorkshop" x1="0" y1="0" x2="0" y2="1">
        <stop offset="0" stop-color="#3f7fb8"/><stop offset="0.5" stop-color="#8aa6bd"/><stop offset="1" stop-color="#2c6d9e"/>
      </linearGradient>
      <linearGradient id="photoPipes" x1="0" y1="0" x2="1" y2="1">
        <stop offset="0" stop-color="#c9d3dc"/><stop offset="0.6" stop-color="#7d8f9f"/><stop offset="1" stop-color="#3c4a56"/>
      </linearGradient>
      <radialGradient id="photoCutting" cx="0.6" cy="0.6" r="0.7">
        <stop offset="0" stop-color="#f08a3c"/><stop offset="0.4" stop-color="#8a4a2a"/><stop offset="1" stop-color="#2a2e35"/>
      </radialGradient>
      <clipPath id="board"><rect x="133" y="107" width="934" height="934"/></clipPath>
    </defs>

    <g clip-path="url(#board)">
      <polygon points="133,107 560,107 590,137 133,137" fill="url(#bandTop)"/>
      <polyline points="133,160 542,160 628,248 664,248" fill="none" stroke="#000" stroke-width="4"/>
      <polygon points="530,107 1067,107 1067,505 898,336 748,336" fill="url(#diagBlue)"/>
      <polygon points="530,107 670,107 898,336 748,336" fill="#0b6fa3" opacity="0.55"/>
      <line x1="761" y1="107" x2="1067" y2="432" stroke="#fff" stroke-width="3"/>

      <ellipse cx="820" cy="700" rx="270" ry="230" fill="url(#glow)"/>

      <polygon points="133,866 133,1041 370,1041 200,895" fill="#00adef"/>
      <line x1="133" y1="900" x2="278" y2="1041" stroke="#fff" stroke-width="3"/>
      <polygon points="208,1008 1067,1008 1067,1041 240,1041" fill="url(#bandBottom)"/>
      <polyline points="208,970 324,970 364,1007 1067,1007" fill="none" stroke="#000" stroke-width="4"/>
      <polygon points="337,940 557,940 606,989 386,989" fill="#00adef"/>
    </g>

    <line x1="438" y1="476" x2="580" y2="476" stroke="#000" stroke-width="3"/>
    <line x1="205" y1="583" x2="496" y2="583" stroke="#000" stroke-width="3"/>

    <polygon role="img" aria-label="Photo of a large industrial fabrication workshop with steel vessels"
      points="831,367 999,462 999,664 831,759 663,664 663,462" fill="url(#photoWorkshop)" stroke="#000" stroke-width="4"/>
    <polygon role="img" aria-label="Photo of a fitter in hi-vis working on pipes and valves"
      points="717,667 811,719 811,833 717,885 623,833 623,719" fill="url(#photoPipes)" stroke="#000" stroke-width="4"/>
    <polygon role="img" aria-label="Photo of a gloved hand cutting steel with a torch and sparks"
      points="924,658 1045,725 1045,863 924,934 804,863 804,725" fill="url(#photoCutting)" stroke="#000" stroke-width="4"/>
  </svg>

  <div class="brand"><span class="brand-dot"></span>KRT Plant Services</div>

  <h1 class="headline-top">We are</h1>
  <div class="headline-main">Hiring!</div>

  <div class="role-lead">LEADING</div>
  <h2 class="role-title">HAND BOILERMAKER<br>&amp; DRAGLINE FITTER</h2>

  <ul class="perks">
    <li>Bowen Basin based</li>
    <li>Dragline &amp; shovel maintenance</li>
    <li>Great pay + long-term work</li>
    <li>Locally owned &amp; operated</li>
  </ul>

  <div class="apply-label">APPLY NOW</div>
  <div class="visit">VISIT OUR WEBSITE</div>
  <div class="url">www.krtplantservices.com</div>
</div>
</body>
</html>
```